Autodetailing namecard design: Rose Gold Lettering on Black Matt

This is a namecard design project
requiring two-sided design
Base Color of Namecard: black matt

On front:
Company name,
"Lumina Finishes 14 Cendana"
Subtext: Auto Detailing Studio

Name of card holder: Marcus Oyelaran
Phone Number: +6011-4837-5062
address: 14, Jalan Cendana 5/3Taman Seri Cendana, 81400 Johor Bahru, Johor, Malaysia

Back:
Our Services
High Gloss Car Paint Protection
Custom Color Modification and Styling
Anti-Chip Glass Protection Film
Heat Rejection Glass Tinting

Target Market(s)

Autodetailing for highend cars

Contact Information for Business Card

as mentioned in project details

Colors

Designer to choose colors to be used in the design.

Requirements
Must have
• The main value-add to this project is the design of a logo suited for our purpose and name, and the inclusion of business card details into the card design

```html
<!DOCTYPE html>
<html lang="en">
<head>
<meta charset="UTF-8">
<title>Lumina Finishes 14 Cendana – Business Card</title>
<link href="https://fonts.googleapis.com/css2?family=Montserrat:wght@400;500&family=Work+Sans:wght@400&display=swap" rel="stylesheet">
<style>
  :root {
    --backdrop: #dedede;
    --card-light: #e6e6e6;
    --card-dark: #404040;
    --rose: #e0877a;
    --white: #ffffff;
  }
  * { margin: 0; padding: 0; box-sizing: border-box; }
  html, body {
    width: 1200px;
    height: 897px;
    overflow: hidden;
    background: var(--backdrop);
  }
  .canvas {
    position: relative;
    width: 1200px;
    height: 897px;
  }
  .card {
    position: absolute;
    left: 329px;
    width: 543px;
    height: 310px;
  }
  .card-front { top: 108px; background: var(--card-light); color: var(--rose); }
  .card-back { top: 479px; background: var(--card-dark); }

  .holder-name {
    position: absolute;
    left: 27px;
    top: 25px;
    font-family: "Work Sans", sans-serif;
    font-size: 24px;
    font-weight: 400;
    letter-spacing: 2px;
    line-height: 1;
  }
  .brand-small {
    position: absolute;
    right: 25px;
    top: 26px;
    text-align: right;
  }
  .brand-small .brand-name {
    font-family: "Montserrat", sans-serif;
    font-weight: 500;
    font-size: 10.5px;
    line-height: 1.2;
  }
  .brand-small .brand-tagline {
    font-family: "Montserrat", sans-serif;
    font-size: 7.5px;
    letter-spacing: 4.6px;
    margin-right: -4.6px;
    line-height: 1.4;
  }
  .contact {
    position: absolute;
    font-family: "Work Sans", sans-serif;
    font-size: 14.5px;
    letter-spacing: 0.8px;
    line-height: 22px;
  }
  .contact-left { left: 27px; bottom: 20px; }
  .contact-right { right: 28px; bottom: 20px; }

  .brand-large {
    position: absolute;
    left: 0;
    right: 0;
    top: 129px;
    text-align: center;
  }
  .brand-large .brand-name {
    font-family: "Montserrat", sans-serif;
    font-weight: 500;
    font-size: 22px;
    color: var(--rose);
    line-height: 1.2;
  }
  .brand-large .brand-tagline {
    font-family: "Montserrat", sans-serif;
    font-size: 16px;
    letter-spacing: 11.5px;
    margin-right: -11.5px;
    color: var(--white);
    line-height: 1.5;
  }
  .services {
    position: absolute;
    left: 0;
    right: 0;
    top: 228px;
    text-align: center;
    font-family: "Work Sans", sans-serif;
  }
  .services-title {
    font-family: "Montserrat", sans-serif;
    font-size: 16px;
    color: var(--rose);
    letter-spacing: 0.5px;
    line-height: 22px;
  }
  .services-list {
    font-size: 14px;
    color: var(--white);
    letter-spacing: 0.4px;
    line-height: 21px;
  }
</style>
</head>
<body>
<main class="canvas">
  <section class="card card-front">
    <h1 class="holder-name">MARCUS OYELARAN</h1>
    <div class="brand-small">
      <div class="brand-name">LUMINA FINISHES 14 CENDANA</div>
      <div class="brand-tagline">AUTO DETAILING STUDIO</div>
    </div>
    <div class="contact contact-left">
      <p>P : +6011-4837-5062</p>
      <p>E : info@marcusoyelaran.com</p>
    </div>
    <div class="contact contact-right">
      <p>W : www.marcusoyelaran.com</p>
    </div>
  </section>

  <section class="card card-back">
    <div class="brand-large">
      <div class="brand-name">LUMINA FINISHES 14 CENDANA</div>
      <div class="brand-tagline">AUTO DETAILING STUDIO</div>
    </div>
    <div class="services">
      <h2 class="services-title">OUR SERVICES</h2>
      <p class="services-list">High Gloss Car Paint Protection | Custom Color Modification and Styling</p>
      <p class="services-list">Anti-Chip Glass Protection Film &nbsp;| Heat Rejection Glass Tinting</p>
    </div>
  </section>
</main>
</body>
</html>
```